KVL cards

Design business cards for renamed business. Korvane Lighting Limited is a leading contract designer of electronic lighting products sepcialising in LED lighting. Need a design that is simple but clear please. Cards for two persons requried.

Target Market(s)

Professional and technical

Industry/Entity Type

Business

Font styles to use
Sans Serif
Other font styles liked:
• tahoma

Colors
ffcf3e

```html
<!DOCTYPE html>
<html lang="en">
<head>
<meta charset="utf-8">
<title>Korvane Lighting Limited – Business Card</title>
<link rel="stylesheet" href="https://fonts.googleapis.com/css2?family=Lato:wght@400;700&display=swap">
<style>
  :root {
    --stage-bg: #6a6a6a;
    --card-bg: #000000;
    --brand-yellow: #ffcf3e;
    --text-light: #f2f2f2;
  }
  html, body {
    margin: 0;
    padding: 0;
    width: 1200px;
    height: 900px;
    overflow: hidden;
    background: var(--stage-bg);
  }
  .stage {
    width: 1200px;
    height: 900px;
    display: flex;
    align-items: center;
    justify-content: center;
  }
  .business-card {
    position: relative;
    width: 1000px;
    height: 580px;
    background: var(--card-bg);
    border-radius: 34px;
    font-family: "Lato", "Tahoma", sans-serif;
    overflow: hidden;
  }
  .company-name {
    position: absolute;
    left: 72px;
    top: 70px;
    margin: 0;
    font-size: 46px;
    font-weight: 400;
    color: var(--brand-yellow);
    letter-spacing: 0.2px;
    white-space: nowrap;
  }
  .person-name {
    position: absolute;
    left: 72px;
    top: 258px;
    margin: 0;
    font-size: 46px;
    font-weight: 400;
    color: var(--brand-yellow);
  }
  .person-name .surname {
    font-weight: 700;
  }
  .contact-list {
    position: absolute;
    left: 72px;
    top: 342px;
    margin: 0;
    padding: 0;
    list-style: none;
    color: var(--text-light);
    font-size: 28px;
    line-height: 38px;
  }
  .contact-item {
    display: flex;
    align-items: flex-start;
  }
  .contact-icon {
    flex: 0 0 24px;
    width: 24px;
    height: 24px;
    margin-top: 8px;
    margin-right: 20px;
    fill: var(--brand-yellow);
  }
  .contact-icon.stroked {
    fill: none;
    stroke: var(--brand-yellow);
    stroke-width: 2.6;
    stroke-linecap: round;
  }
  .led-illustration {
    position: absolute;
    left: 612px;
    top: 300px;
    width: 300px;
    height: 210px;
    border-radius: 14px;
    background: linear-gradient(90deg,
      rgba(255, 40, 40, 0.55) 0%,
      rgba(255, 150, 30, 0.55) 18%,
      rgba(255, 220, 40, 0.55) 36%,
      rgba(60, 220, 70, 0.55) 55%,
      rgba(40, 190, 255, 0.55) 75%,
      rgba(240, 60, 200, 0.55) 100%);
  }
</style>
</head>
<body>
  <main class="stage">
    <section class="business-card">
      <h1 class="company-name">Korvane Lighting Limited</h1>

      <h2 class="person-name">Alden <span class="surname">Marsh</span></h2>

      <ul class="contact-list">
        <li class="contact-item">
          <svg class="contact-icon" viewBox="0 0 24 24" aria-hidden="true">
            <path d="M2 9c0-3 4-5 10-5s10 2 10 5v2h-5V8.5c-1.5-.6-3.2-.9-5-.9s-3.5.3-5 .9V11H2z"/>
            <path d="M6 12l2-3h8l2 3v8H6z"/>
          </svg>
          <span>555-014-2290</span>
        </li>
        <li class="contact-item">
          <svg class="contact-icon" viewBox="0 0 24 24" aria-hidden="true">
            <path d="M2 5h20v14H2z"/>
            <path d="M3 6l9 7 9-7" fill="none" stroke="#000" stroke-width="2"/>
          </svg>
          <span>korvanelighting.com</span>
        </li>
        <li class="contact-item">
          <svg class="contact-icon stroked" viewBox="0 0 24 24" aria-hidden="true">
            <path d="M10 14l4-4"/>
            <path d="M8.5 11.5l-3 3a3 3 0 004.2 4.2l3-3"/>
            <path d="M15.5 12.5l3-3a3 3 0 00-4.2-4.2l-3 3"/>
          </svg>
          <span>alden@korvanelighting.com</span>
        </li>
        <li class="contact-item">
          <svg class="contact-icon" viewBox="0 0 24 24" aria-hidden="true">
            <path d="M12 3l10 9h-3v9h-5v-6h-4v6H5v-9H2z"/>
          </svg>
          <span>18 Harrow Lane,<br>Suite #210, Elm Court, NY 10452</span>
        </li>
      </ul>

      <div class="led-illustration" role="img" aria-label="Row of six glowing LEDs in red, orange, yellow, green, blue and pink"></div>
    </section>
  </main>
</body>
</html>
```